Brava Stone Oven Kitchen (restaurant)

Restaurant with a cool vibe.
We need a refresh of existing site. Appealing to a hip crowd of 25 or older age bracket (mid price to high small town). Constant changes food and cocktail menu. A vibing atmosphere with jazz funk hip music.
Must be able to scale for any device… phone/mobile device super important.
Instagram: @Brava.Linwell
Website: bravalinwell.example

Target Market(s)

25-55 age group

Number of Pages Required

1 page

Font styles to use
Sans Serif

Requirements
Must have
• Simple to navigate. Simplicity is the key to all sophistication.

Links/Buttons
Menu
Gift Cards
Reservations
Take Out
Contact Us
Should not have
• Please, nothing generic looking… no cookie cutter look. Originality

```html
<!DOCTYPE html>
<html lang="en">
<head>
<meta charset="utf-8">
<title>Brava Stone Oven Kitchen</title>
<link rel="stylesheet" href="https://fonts.googleapis.com/css2?family=Arvo:wght@400;700&family=Lato:wght@400;700&display=swap">
<style>
:root{
  --accent:#f15a24;
  --ink:#222222;
  --muted:#555555;
  --line:#cfcfcf;
  --dark:#2a2a2a;
  --darker:#1f1f1f;
  --paper:#ffffff;
  --mist:#f4f4f4;
  --star:#f6c23e;
}
*{margin:0;padding:0;box-sizing:border-box}
html,body{width:1200px;height:5357px;overflow:hidden}
body{position:relative;background:var(--paper);font-family:"Lato",sans-serif;color:var(--ink)}
.abs{position:absolute}
h2,h3,.slab{font-family:"Arvo",serif;font-weight:400}
p{font-size:13px;line-height:26px;color:var(--muted)}

/* hero */
.hero{left:0;top:0;width:1200px;height:750px;background:radial-gradient(ellipse at 50% 65%,#9a5a2e 0%,#5b3a24 40%,#2b2522 75%,#1c1c1c 100%)}
.hero-shade{left:0;top:0;width:1200px;height:750px;background:linear-gradient(180deg,rgba(0,0,0,.55),rgba(0,0,0,.15) 45%,rgba(0,0,0,.1))}
.nav{left:0;top:44px;width:1200px;height:30px}
.nav a{position:absolute;top:6px;color:#fff;font-size:13px;text-decoration:none}
.brand{position:absolute;top:0;left:500px;width:200px;text-align:center;color:#fff;font-family:"Lato",sans-serif;font-weight:700}
.brand .name{display:block;font-size:24px;letter-spacing:2px;line-height:24px}
.brand .sub{display:block;font-size:9px;line-height:11px}
.hero-title{left:250px;top:290px;width:700px;height:120px}
.hero-copy{left:320px;top:388px;width:560px;text-align:center;color:#fff;font-size:13px;line-height:27px}
.btn{display:block;background:var(--accent);color:#fff;font-size:12px;text-align:center;text-transform:uppercase;text-decoration:none}
.hero-btn{left:514px;top:463px;width:170px;height:44px;line-height:44px}

/* restaurant */
.photo{display:block}
.rest-photo{left:154px;top:869px;width:445px;height:333px;background:linear-gradient(180deg,#a9c2da 0%,#c9d6e2 30%,#8a4a34 32%,#6e3b2a 80%,#3a3a3a 100%)}
.rest-text{left:661px;top:930px;width:400px}
.rest-text h2{font-size:30px;margin-bottom:20px}

/* why */
.why{left:0;top:1273px;width:1200px;height:610px;background:radial-gradient(ellipse at 20% 70%,#6b5a3e,#2e2a25 55%,#1e1e1e)}
.why-title{left:0;top:1428px;width:1200px;text-align:center;color:#fff;font-size:30px}
.why-copy{left:290px;top:1484px;width:620px;text-align:center;color:#fff}
.card{background:#fff;width:291px;height:291px;top:1587px;text-align:center;box-shadow:0 6px 18px rgba(0,0,0,.12)}
.card svg{margin-top:40px}
.card h3{font-size:17px;margin:22px 0 14px}
.card p{width:210px;margin:0 auto;line-height:27px}

/* menu */
.menu-title{left:0;top:1955px;width:1200px;text-align:center;font-size:30px}
.tabs{left:0;top:2014px;width:1200px;text-align:center;font-size:12px}
.tabs span{margin:0 11px;color:var(--muted)}
.tabs .on{color:var(--accent)}
.tab-mark{left:818px;top:2038px;width:30px;height:2px;background:var(--accent)}
.dish{width:400px}
.dish h3{font-size:17px;margin-bottom:22px}
.dish .price{position:absolute;right:0;top:0;color:var(--accent);font-family:"Arvo",serif;font-size:17px}
.dish p{width:270px}
.rule{height:1px;background:var(--line)}

/* team */
.team{left:0;top:2680px;width:1200px;height:680px;background:var(--mist)}
.team-text{left:152px;top:2950px;width:400px}
.team-text h2{font-size:30px;margin-bottom:22px}
.team-photo{left:601px;top:2818px;width:447px;height:500px;background:linear-gradient(160deg,#5a4030,#2e2622 60%,#1b1b1b)}

/* testimonials */
.testi{left:0;top:3353px;width:1200px;height:610px;background:radial-gradient(ellipse at 50% 50%,#4a3a30,#2a2624 60%,#1d1d1d)}
.testi-title{left:0;top:3525px;width:1200px;text-align:center;color:#fff;font-size:30px}
.quote{left:250px;top:3602px;width:700px;text-align:center;color:#fff;line-height:27px}
.qmark{color:#fff;font-family:"Arvo",serif;font-size:54px;font-weight:700;line-height:1}
.testi-name{left:0;top:3734px;width:1200px;text-align:center;color:#fff;font-size:22px}
.stars{left:0;top:3785px;width:1200px;text-align:center;color:var(--star);font-size:16px;letter-spacing:2px}

/* booking */
.book-title{left:0;top:3968px;width:1200px;text-align:center;font-size:30px}
.book-copy{left:0;top:4035px;width:1200px;text-align:center}
.field{top:4127px;width:290px;height:44px;border:1.5px solid #333;font-size:12px;color:var(--muted);padding:0 18px;line-height:41px}
.field svg{position:absolute;right:14px;top:13px}
.book-btn{left:518px;top:4227px;width:168px;height:44px;line-height:44px}

/* gallery + map */
.tile{top:4351px;width:240px;height:246px}
.map{left:0;top:4597px;width:1200px;height:353px;background:linear-gradient(135deg,#e9ecef,#dfe6dc 45%,#e7e9ee)}

/* footer */
.footer{left:0;top:4950px;width:1200px;height:327px;background:var(--dark)}
.footer-brand{left:400px;top:4985px;width:400px;text-align:center;color:#fff;font-weight:700}
.footer-brand .name{display:block;font-size:40px;letter-spacing:3px;line-height:42px}
.footer-brand .sub{display:block;font-size:14px}
.fcol{top:5094px;color:#fff}
.fcol h4{font-family:"Arvo",serif;font-weight:400;font-size:18px;margin-bottom:28px}
.fcol .line{font-size:12px;line-height:29px;display:flex;align-items:center;gap:12px}
.bar{left:0;top:5277px;width:1200px;height:80px;background:var(--darker)}
.socials{left:534px;top:5289px;width:132px;display:flex;gap:10px}
.socials span{width:25px;height:25px;border:1.5px solid #fff;border-radius:50%}
.copy{left:0;top:5329px;width:1200px;text-align:center;color:#fff;font-size:11px}
</style>
</head>
<body>

<!-- hero -->
<div class="abs hero" role="img" aria-label="Wood fired pizza topped with fresh arugula in front of the stone oven"></div>
<div class="abs hero-shade"></div>
<svg class="abs" style="left:0;top:620px" width="1200" height="131" viewBox="0 0 1200 131"><path d="M0 30 Q600 170 1200 30 L1200 131 L0 131Z" fill="#fff"/></svg>
<nav class="abs nav">
  <a href="#" style="left:288px">Area for</a>
  <a href="#" style="left:365px">Gift Cards</a>
  <a href="#" style="left:452px">Menu</a>
  <div class="brand"><span class="name">BRAVA</span><span class="sub">Stone Oven Kitchen</span></div>
  <a href="#" style="left:704px">Contact Us</a>
  <a href="#" style="left:797px">Reservations</a>
  <a href="#" style="left:900px">Take Out</a>
</nav>
<svg class="abs hero-title" viewBox="0 0 700 120">
  <path id="arc" d="M20 110 Q350 20 680 110" fill="none"/>
  <text font-family="Arvo, serif" font-weight="700" font-size="48" fill="#fff" text-anchor="middle"><textPath href="#arc" startOffset="50%">Good Foods, Great Vibes</textPath></text>
</svg>
<p class="abs hero-copy">A neighborhood restaurant in the heart of Linwell. Offering a unique menu of stone oven eats, craft beer, cocktails and wine.</p>
<a href="#" class="abs btn hero-btn">View our menu</a>

<!-- our restaurant -->
<div class="abs photo rest-photo" role="img" aria-label="Red brick corner building housing the restaurant"></div>
<div class="abs rest-text">
  <h2>Our Restaurant</h2>
  <p>Lorem Ipsum is simply dummy text of the printing and typesetting industry. Lorem Ipsum has been the industry's standard dummy text ever since the 1500s, when an unknown printer took a galley of type and scrambled it to make a type specimen book. It has survived not only five centuries, but also the leap into electronic typesetting, remaining essentially unchanged.</p>
</div>

<!-- why choose us -->
<div class="abs why" role="img" aria-label="Overhead view of dishes on a dark table"></div>
<svg class="abs" style="left:0;top:1272px" width="1200" height="90" viewBox="0 0 1200 90"><path d="M0 0 L1200 0 L1200 10 Q600 110 0 10Z" fill="#fff"/></svg>
<svg class="abs" style="left:0;top:1840px" width="1200" height="44" viewBox="0 0 1200 44"><path d="M0 44 Q600 -10 1200 44Z" fill="#fff"/></svg>
<h2 class="abs why-title">Why Choose us?</h2>
<p class="abs why-copy">Lorem Ipsum is simply dummy text of the printing and typesetting industry. Lorem Ipsum has been the industry's standard dummy text ever since the 1500s.</p>

<div class="abs card" style="left:146px">
  <svg width="54" height="54" viewBox="0 0 54 54" fill="none" stroke="#222" stroke-width="2"><rect x="14" y="6" width="28" height="36" rx="2"/><path d="M20 16h16M20 22h16M20 28h10"/><path d="M6 42h42v6H6z"/></svg>
  <h3>Menu for every taste</h3>
  <p>Lorem Ipsum is simply dummy text of the printing and typesetting industry.</p>
</div>
<div class="abs card" style="left:449px">
  <svg width="64" height="54" viewBox="0 0 64 54" fill="none" stroke="#222" stroke-width="2"><circle cx="22" cy="32" r="12"/><circle cx="42" cy="32" r="12"/><path d="M32 20c0-8 4-12 10-14M8 46h48"/></svg>
  <h3>Always fresh ingredients</h3>
  <p>Lorem Ipsum is simply dummy text of the printing and typesetting industry.</p>
</div>
<div class="abs card" style="left:751px">
  <svg width="54" height="54" viewBox="0 0 54 54" fill="none" stroke="#222" stroke-width="2"><path d="M16 22a8 8 0 0 1 4-14 9 9 0 0 1 14 0 8 8 0 0 1 4 14v8H16z"/><path d="M18 30v14h18V30"/></svg>
  <h3>Experienced chefs</h3>
  <p>Lorem Ipsum is simply dummy text of the printing and typesetting industry.</p>
</div>

<!-- menu -->
<h2 class="abs menu-title">Our Menu</h2>
<div class="abs tabs"><span>Shareables</span><span>Stone Oven Pizza</span><span>Salads</span><span>Sandwiches</span><span>Burgers</span><span class="on">Mains &amp; Pasta</span></div>
<div class="abs tab-mark"></div>

<div class="abs dish" style="left:150px;top:2122px"><h3>Sonoma Valley Pasta</h3><span class="price">$25</span><p>Grilled sausage, baby spinach, green peas, cremini mushroom, white wine &amp; butter, fresh ricotta, orecchiette pasta</p></div>
<div class="abs dish" style="left:617px;top:2122px"><h3>Chicken Souvlaki</h3><span class="price">$25</span><p>Grilled lemon &amp; herbed chicken skewers, house-made tzatziki, Greek village salad, garlic parm fries</p></div>
<div class="abs rule" style="left:150px;top:2265px;width:375px"></div>
<div class="abs rule" style="left:617px;top:2265px;width:434px"></div>
<div class="abs dish" style="left:150px;top:2289px"><h3>Shrimp Linguine</h3><span class="price">$27</span><p>Wild Argentinian shrimp, bay scallops, fresh lemon, sun-dried tomato, parmesan, butter &amp; white wine sauce, linguini pasta</p></div>
<div class="abs dish" style="left:617px;top:2289px"><h3>Buttermilk Fried Tenders</h3><span class="price">$20</span><p>Buttermilk fried chicken tenders, homemade jalapeño ranch &amp; garlic aioli for dipping, garlic parm fries</p></div>
<div class="abs rule" style="left:150px;top:2434px;width:375px"></div>
<div class="abs dish" style="left:150px;top:2461px"><h3>Monterey Chicken</h3><span class="price">$25</span><p>Grilled chicken breast, garlic &amp; cilantro ricotta, fresh spinach, cremini mushroom, chickpeas, sweet corn</p></div>

<!-- team -->
<div class="abs team"></div>
<svg class="abs" style="left:0;top:2679px" width="1200" height="80" viewBox="0 0 1200 80"><path d="M0 0 L1200 0 L1200 75 Q600 -15 0 75Z" fill="#fff"/></svg>
<div class="abs team-text">
  <h2>Meet Our Team</h2>
  <p>Lorem Ipsum is simply dummy text of the printing and typesetting industry. Lorem Ipsum has been the industry's standard dummy text ever since the 1500s, when an unknown printer took a galley of type and scrambled it to make a type specimen book. It has survived not only five centuries, but also the leap into electronic typesetting, remaining essentially unchanged.</p>
</div>
<div class="abs photo team-photo" role="img" aria-label="The restaurant team posing together in front of the oven"></div>

<!-- testimonials -->
<div class="abs testi" role="img" aria-label="Dim view of the dining room"></div>
<svg class="abs" style="left:0;top:3352px" width="1200" height="60" viewBox="0 0 1200 60"><path d="M0 0 L1200 0 L1200 10 Q600 60 0 0Z" fill="#f4f4f4"/></svg>
<svg class="abs" style="left:0;top:3880px" width="1200" height="84" viewBox="0 0 1200 84"><path d="M0 0 Q600 100 1200 84 L0 84Z" fill="#fff"/></svg>
<h2 class="abs testi-title">Testimonials</h2>
<svg class="abs" style="left:68px;top:3632px" width="44" height="20" viewBox="0 0 44 20"><path d="M42 10H4M12 2L3 10l9 8" fill="none" stroke="#fff" stroke-width="2"/></svg>
<svg class="abs" style="left:1084px;top:3632px" width="44" height="20" viewBox="0 0 44 20"><path d="M2 10h38M32 2l9 8-9 8" fill="none" stroke="#fff" stroke-width="2"/></svg>
<span class="abs qmark" style="left:220px;top:3600px">“</span>
<p class="abs quote">Lorem Ipsum is simply dummy text of the printing and typesetting industry. Lorem Ipsum has been the industry's standard dummy text ever since the 1500s, when an unknown printer took a galley of type and scrambled it to make a type specimen book. It has survived not only five centuries, but also the leap into electronic typesetting, remaining essentially unchanged.</p>
<span class="abs qmark" style="left:690px;top:3688px">”</span>
<div class="abs slab testi-name">Marco Dell</div>
<div class="abs stars">★★★★★</div>

<!-- booking -->
<h2 class="abs book-title">Book a table</h2>
<p class="abs book-copy">Reservations will not be available for the courtyard under phase 1 and 2 of reopening. Walk-ins only.<br>We can't wait to see you!</p>
<div class="abs field" style="left:152px">How many persons?<svg width="16" height="16" viewBox="0 0 16 16" fill="none" stroke="#333" stroke-width="1.4"><circle cx="8" cy="5" r="3.5"/><path d="M1.5 15c1-4 12-4 13 0"/></svg></div>
<div class="abs field" style="left:458px">In which date<svg width="16" height="16" viewBox="0 0 16 16" fill="none" stroke="#333" stroke-width="1.4"><rect x="1.5" y="3" width="13" height="11.5"/><path d="M1.5 7h13M5 1v4M11 1v4"/></svg></div>
<div class="abs field" style="left:765px">Which Time?<svg width="16" height="16" viewBox="0 0 16 16" fill="none" stroke="#333" stroke-width="1.4"><circle cx="8" cy="8" r="6.5"/><path d="M8 4v4l3 2"/></svg></div>
<a href="#" class="abs btn book-btn">Reservation</a>

<!-- gallery -->
<div class="abs tile" style="left:0;background:linear-gradient(135deg,#7a4a2a,#c08a4a 50%,#4a3a2a)" role="img" aria-label="Tacos with red cabbage"></div>
<div class="abs tile" style="left:240px;background:linear-gradient(135deg,#d9c27a,#f1e3b0 50%,#8a9a5a)" role="img" aria-label="Grilled sandwich halves"></div>
<div class="abs tile" style="left:480px;background:linear-gradient(135deg,#5a3a28,#b4622f 50%,#6a7a3a)" role="img" aria-label="Stone oven pizza"></div>
<div class="abs tile" style="left:720px;background:linear-gradient(135deg,#3a3a3a,#c9a050 50%,#6a5030)" role="img" aria-label="Fried chicken tenders with sauces"></div>
<div class="abs tile" style="left:960px;background:linear-gradient(135deg,#a9b4bf,#8a5a3a 50%,#3a2a22)" role="img" aria-label="Stacked burger"></div>

<!-- map -->
<div class="abs map" role="img" aria-label="Street map showing the restaurant location"></div>
<svg class="abs" style="left:588px;top:4780px" width="24" height="34" viewBox="0 0 24 34"><path d="M12 33C4 21 1 16 1 11a11 11 0 0 1 22 0c0 5-3 10-11 22z" fill="#e53935"/><circle cx="12" cy="11" r="4" fill="#fff"/></svg>

<!-- footer -->
<div class="abs footer"></div>
<div class="abs footer-brand"><span class="name">BRAVA</span><span class="sub">Stone Oven Kitchen</span></div>
<div class="abs fcol" style="left:152px">
  <h4>Contact info.</h4>
  <div class="line"><svg width="16" height="16" viewBox="0 0 16 16"><path d="M3 1l3 3-2 2c1 2 3 4 5 5l2-2 3 3-2 3C7 15 1 9 1 3z" fill="#fff"/></svg>555-014-2288</div>
  <div class="line"><svg width="16" height="12" viewBox="0 0 16 12"><rect x="0.5" y="0.5" width="15" height="11" fill="none" stroke="#fff"/><path d="M1 1l7 6 7-6" fill="none" stroke="#fff"/></svg>hello@bravalinwell.example</div>
</div>
<div class="abs fcol" style="left:526px">
  <h4>Dining Hours</h4>
  <div class="line">Courtyard is open</div>
  <div class="line">Thu to Sun 12:00pm – 9:00pm</div>
</div>
<div class="abs fcol" style="left:838px">
  <h4>Pickup &amp; Kitchen Hours</h4>
  <div class="line">Thu to Sun 12:00pm – 8:00pm</div>
</div>
<div class="abs bar"></div>
<div class="abs socials"><span></span><span></span><span></span><span></span></div>
<div class="abs copy">Copyright © 2021 Brava stone oven kitchen. All Rights Reserved</div>

</body>
</html>
```